Venbrook Finishes website

Epoxy Resin Flooring for home renovations and commercial property.
3 page website homepage, contact us and gallery with a link to Instagram.
Looking for someone to create a visually pleasing website for home transformation and design. I have attached some designs of completed work however I can send you many more. Use colour and don’t inspiration from the logo. If happy with stage one we will add a commercial page as a new project.

Target Market(s)

Homeowners that want to improve their home or rental property

Industry/Entity Type

Home improvements

Coding

Coded - Design and coding required

Number of Pages Required

3 page

Requirements
Must have
• Home Page, Contact Us page and showcase / gallery page
Nice to have
• I would like the colour theme to be taken from the logo, a clean finish with artistic usuals to get homeowners excited about their project

```html
<!DOCTYPE html>
<html lang="en">
<head>
<meta charset="utf-8">
<title>Venbrook Finishes – Epoxy Resin Flooring</title>
<link href="https://fonts.googleapis.com/css2?family=Poppins:ital,wght@0,400;0,500;0,600;0,700;0,800;1,400&display=swap" rel="stylesheet">
<style>
:root{
  --red:#ec1c24;
  --red-soft:#fdecee;
  --ink:#1b1b1b;
  --body:#4a4a4a;
  --dark:#23262e;
  --black:#000;
  --white:#fff;
  --line:#d9d9d9;
}
*{margin:0;padding:0;box-sizing:border-box}
html,body{width:1200px;height:4208px;overflow:hidden;background:var(--white)}
body{position:relative;font-family:"Poppins",sans-serif;color:var(--ink)}
.abs{position:absolute}
.btn{position:absolute;background:var(--red);color:var(--white);font-size:12px;font-weight:500;display:flex;align-items:center;justify-content:center}
.ph{position:absolute}

/* header */
.nav a{position:absolute;top:22px;font-size:12px;color:var(--ink);text-decoration:none;font-weight:500}
.nav a.active{color:var(--red);border-bottom:1px solid var(--red);padding-bottom:2px}
.brand{position:absolute;left:0;top:0;width:300px;height:125px;background:var(--white);z-index:3}
.brand .mark{position:absolute;left:54px;top:28px;width:58px;height:58px;background:var(--red)}
.brand .name{position:absolute;left:124px;top:30px;font-size:22px;font-weight:700;line-height:1.05;color:var(--ink)}
.brand .phone{position:absolute;left:126px;top:72px;font-size:15px;color:var(--ink)}

/* hero */
.hero{position:absolute;left:0;top:70px;width:1200px;height:600px;background:linear-gradient(100deg,#2a2a2a 0%,#4a4845 45%,#6b4a3e 70%,#4b5a3a 100%)}
.hero-shade{position:absolute;inset:0;background:linear-gradient(90deg,rgba(0,0,0,.55),rgba(0,0,0,.15))}
.hero h1{position:absolute;left:140px;top:188px;font-size:33px;font-weight:700;line-height:46px;color:var(--white);width:600px}
.hero p{position:absolute;left:142px;top:300px;font-size:16px;line-height:28px;color:var(--white);width:460px}
.hero .word{position:absolute;left:295px;top:408px;font-size:32px;font-weight:600;color:var(--white);letter-spacing:1px}
.dots span{position:absolute;top:516px;width:12px;height:12px;border-radius:50%;background:#bbb}

/* about */
.about h2{position:absolute;left:635px;top:780px;font-size:36px;font-weight:700;letter-spacing:1px}
.about .lead{position:absolute;left:635px;top:842px;width:420px;font-size:13.5px;font-weight:600;line-height:23px}
.about .text{position:absolute;left:635px;top:916px;width:420px;font-size:13.5px;line-height:23px;color:var(--body)}

/* sections */
.sec-title{position:absolute;left:0;width:1200px;text-align:center;font-size:31px;font-weight:700}
.card{position:absolute;top:1352px;width:222px;height:305px;background:var(--red-soft)}
.card .ph{left:0;top:0;width:222px;height:142px}
.card h3{position:absolute;left:27px;top:168px;font-size:16px;font-weight:600}
.card p{position:absolute;left:27px;top:194px;width:180px;font-size:11.5px;line-height:18px;color:var(--body)}
.card a{position:absolute;left:27px;top:256px;font-size:11.5px;font-weight:600;color:var(--red)}
.card.on{background:var(--red)}
.card.on h3,.card.on p,.card.on a{color:var(--white)}

/* testimonial */
.testi{position:absolute;left:0;top:1837px;width:1200px;height:542px;background:var(--dark)}
.testi h2{position:absolute;left:650px;top:90px;font-size:28px;font-weight:700;color:var(--white)}
.arrow-btn{position:absolute;width:34px;height:34px;border-radius:50%;background:var(--white);display:flex;align-items:center;justify-content:center}
.quote{position:absolute;left:490px;top:217px;width:521px;height:232px;background:var(--white)}
.quote-foot{position:absolute;left:522px;top:449px;width:459px;height:26px;background:var(--white)}
.quote p{position:absolute;left:80px;top:62px;width:361px;text-align:center;font-style:italic;font-size:13px;line-height:23px;color:var(--body)}
.quote h4{position:absolute;left:0;top:151px;width:521px;text-align:center;font-size:16px;font-weight:600}
.quote span{position:absolute;left:0;top:178px;width:521px;text-align:center;font-size:12px}

/* why */
.why{position:absolute;left:0;top:2379px;width:1200px;height:356px;background:linear-gradient(90deg,#e41e26,#ee2a2f 50%,#e51d25)}
.why h2{position:absolute;top:68px;left:0;width:1200px;text-align:center;font-size:31px;font-weight:700;color:var(--white)}
.feat{position:absolute;top:158px;width:200px;text-align:center;color:var(--white)}
.feat svg{display:block;margin:0 auto}
.feat h3{font-size:14px;font-weight:500;margin-top:8px}
.feat p{font-size:9.5px;line-height:15px;margin-top:4px}
.feat .more{font-size:16px;margin-top:8px}

/* gallery */
.g{position:absolute;width:229px;height:228px}

/* contact */
.contact-bg{position:absolute;left:0;top:3824px;width:1200px;height:384px;background:var(--black)}
.contact h2{position:absolute;left:0;top:3608px;width:1200px;text-align:center;font-size:33px;font-weight:700;color:var(--ink)}
.field{position:absolute;height:33px;background:var(--white);font-size:11px;color:#555;padding:10px 16px}

/* footer */
.fnav a{position:absolute;top:3967px;font-size:13px;color:var(--white);text-decoration:none}
.fnav a.active{color:var(--red)}
.finfo{position:absolute;font-size:13px;line-height:22px;color:var(--white)}
.fdiv{position:absolute;top:4030px;width:1px;height:90px;background:#444}
.social{position:absolute;top:4161px;width:22px;height:22px;border-radius:50%;background:var(--red)}
</style>
</head>
<body>

<!-- Header -->
<div class="brand">
  <div class="mark"></div>
  <div class="name">VENBROOK<br>FINISHES</div>
  <div class="phone">0400 318 256</div>
</div>
<nav class="nav">
  <a class="active" style="left:558px">Home</a>
  <a style="left:635px">Services</a>
  <a style="left:725px">Gallery</a>
  <a style="left:807px">Contact</a>
</nav>
<div class="btn" style="left:884px;top:10px;width:174px;height:41px">Get A Free Estimate</div>

<!-- Hero -->
<section class="hero">
  <div class="ph" role="img" aria-label="Covered patio of a brick home with dark epoxy resin floor tiles" style="inset:0"></div>
  <div class="hero-shade"></div>
  <h1>Elevate Your Space with Stunning Epoxy Resin Flooring.a</h1>
  <p>Briefly mention your services and target market. Example: "Transform your home with our durable and stylish epoxy resin solutions.</p>
  <div class="btn" style="left:142px;top:407px;width:131px;height:42px">Get a Quote</div>
  <div class="word">VENBROOK</div>
  <div class="dots">
    <span style="left:144px"></span>
    <span style="left:174px;background:var(--red);box-shadow:0 0 0 3px #fff"></span>
    <span style="left:205px"></span>
    <span style="left:236px"></span>
  </div>
</section>

<!-- About -->
<section class="about">
  <div class="abs" style="left:126px;top:741px;width:1px;height:377px;background:#555"></div>
  <div class="ph" role="img" aria-label="White bathroom with freestanding bath and grey epoxy floor" style="left:136px;top:741px;width:218px;height:377px;background:linear-gradient(160deg,#e9e9e9,#b9b9b9 60%,#6e6e6e)"></div>
  <div class="ph" role="img" aria-label="Shower room with glass screen and dark tiled epoxy floor" style="left:372px;top:805px;width:217px;height:379px;background:linear-gradient(180deg,#f2f2f2,#d0d0d0 55%,#575757)"></div>
  <div class="abs" style="left:599px;top:805px;width:1px;height:375px;background:#555"></div>
  <h2>About</h2>
  <p class="lead">Lorem ipsum dolor sit amet, consectetuer adipiscing elit, sed diam nonummy nibh euismod tincidunt ut laoreet dolore magna aliquam erat volutpat.</p>
  <p class="text">Ut wisi enim ad minim veniam, quis nostrud exerci tation ullamcorper suscipit lobortis nisl ut aliquip ex ea commodo consequat. Duis autem vel eum iriure dolor in hendrerit in vulputate velit esse molestie consequat, vel illum dolore eu feugiat nulla facilisis at vero eros et accumsan et iusto odio dignissim qui blandit praesent luptatum zzril delenit augue duis dolore te feugait nulla facilisi.</p>
  <div class="btn" style="left:635px;top:1094px;width:131px;height:39px">Read More</div>
</section>

<!-- Services -->
<h2 class="sec-title" style="top:1265px">Our Services</h2>
<div class="card" style="left:140px">
  <div class="ph" role="img" aria-label="Residential apartment towers under blue sky" style="background:linear-gradient(180deg,#6aa3e0,#9cb6c8 55%,#6d7a5c)"></div>
  <h3>Residential</h3><p>Lorem ipsum dolor sit amet, consectetur adipiscing elit, sed odo viverra maecenas ac</p><a>Read More</a>
</div>
<div class="card" style="left:372px">
  <div class="ph" role="img" aria-label="Modern glass commercial building" style="background:linear-gradient(180deg,#c9d8e6,#7f8f99 60%,#5c6b4d)"></div>
  <h3>Commercial</h3><p>Lorem ipsum dolor sit amet, consectetur adipiscing elit, sed odo viverra maecenas ac</p><a>Read More</a>
</div>
<div class="card on" style="left:604px">
  <div class="ph" role="img" aria-label="Worker installing roof shingles" style="background:linear-gradient(160deg,#6d6a66,#9a9793 55%,#c9c9c9)"></div>
  <h3>Installation</h3><p>Lorem ipsum dolor sit amet, consectetur adipiscing elit, sed odo viverra maecenas ac</p><a>Read More</a>
</div>
<div class="card" style="left:836px">
  <div class="ph" role="img" aria-label="Worker repairing a roof" style="background:linear-gradient(180deg,#cfd8e0,#8a7f76 55%,#5b5550)"></div>
  <h3>Repairs</h3><p>Lorem ipsum dolor sit amet, consectetur adipiscing elit, sed odo viverra maecenas ac</p><a>Read More</a>
</div>
<div class="btn" style="left:534px;top:1709px;width:132px;height:41px">Contact Us</div>

<!-- Testimonial -->
<section class="testi">
  <div class="ph" role="img" aria-label="Portrait of a smiling businessman in a suit in an office" style="left:0;top:0;width:602px;height:542px;background:linear-gradient(135deg,#4c4e52,#8b8f93 50%,#3c3f44)"></div>
  <svg class="abs" style="left:270px;top:244px" width="58" height="58" viewBox="0 0 58 58"><circle cx="29" cy="29" r="29" fill="#ec1c24"/><path d="M23 18 L41 29 L23 40 Z" fill="#fff"/></svg>
  <h2>Testimonial</h2>
  <div class="abs" style="left:650px;top:138px;width:70px;height:3px;background:var(--red);border-radius:2px"></div>
  <div class="arrow-btn" style="left:973px;top:69px"><svg width="12" height="12" viewBox="0 0 12 12"><path d="M8 2 L4 6 L8 10" stroke="#ec1c24" stroke-width="2" fill="none"/></svg></div>
  <div class="arrow-btn" style="left:973px;top:115px"><svg width="12" height="12" viewBox="0 0 12 12"><path d="M4 2 L8 6 L4 10" stroke="#ec1c24" stroke-width="2" fill="none"/></svg></div>
  <svg class="abs" style="left:700px;top:169px" width="100" height="50" viewBox="0 0 100 50"><path d="M4 50 A46 46 0 0 1 96 50" fill="#fff" stroke="#8a8a8a" stroke-width="6"/></svg>
  <div class="quote-foot"></div>
  <div class="quote">
    <svg class="abs" style="left:249px;top:0" width="22" height="18" viewBox="0 0 22 18"><path d="M0 18 V9 Q0 1 9 0 V4 Q4 5 4 9 H9 V18 Z M12 18 V9 Q12 1 21 0 V4 Q16 5 16 9 H21 V18 Z" fill="#ec1c24"/></svg>
    <p>Hemos realizado un aumento exponencial de reservas. Además he podido controlar los paros de ventas desde el móvil.</p>
    <h4>- Marco Delvane</h4>
    <span>Director Hotel Castellan Court</span>
  </div>
</section>

<!-- Why choose -->
<section class="why">
  <h2>Why Choose Epoxy Resin Flooring?</h2>
  <div class="feat" style="left:138px">
    <svg width="40" height="40" viewBox="0 0 40 40" fill="none" stroke="#fff" stroke-width="2"><rect x="4" y="16" width="20" height="10" rx="5" transform="rotate(-45 14 21)"/><rect x="16" y="14" width="20" height="10" rx="5" transform="rotate(-45 26 19)"/></svg>
    <h3>durability</h3><p>Lorem ipsum dolor sit amet, consectetur Quis commodo viverra accumsan lacus vel facilisis.</p><div class="more">»</div>
  </div>
  <div class="feat" style="left:378px">
    <svg width="40" height="40" viewBox="0 0 40 40" fill="none" stroke="#fff" stroke-width="2"><circle cx="20" cy="10" r="5"/><path d="M10 36 V24 Q10 18 20 18 Q30 18 30 24 V36"/><path d="M14 36 H26"/></svg>
    <h3>Style</h3><p>Lorem ipsum dolor sit amet, consectetur Quis commodo viverra accumsan lacus vel facilisis.</p><div class="more">»</div>
  </div>
  <div class="feat" style="left:618px">
    <svg width="40" height="40" viewBox="0 0 40 40" fill="none" stroke="#fff" stroke-width="2"><circle cx="20" cy="20" r="14"/><circle cx="20" cy="20" r="6"/><path d="M20 2 V8 M20 32 V38 M2 20 H8 M32 20 H38"/></svg>
    <h3>Low Maintenance</h3><p>Lorem ipsum dolor sit amet, consectetur Quis commodo viverra accumsan lacus vel facilisis.</p><div class="more">»</div>
  </div>
  <div class="feat" style="left:860px">
    <svg width="40" height="40" viewBox="0 0 40 40" fill="none" stroke="#fff" stroke-width="2"><circle cx="20" cy="20" r="13" stroke-dasharray="5 3"/><circle cx="20" cy="20" r="5"/></svg>
    <h3>Customization</h3><p>Lorem ipsum dolor sit amet, consectetur Quis commodo viverra accumsan lacus vel facilisis.</p><div class="more">»</div>
  </div>
</section>

<!-- Gallery -->
<h2 class="sec-title" style="top:2810px">Our Gallery</h2>
<div class="g" role="img" aria-label="Glossy living room floor with warm lit fireplace" style="left:0;top:2900px;background:linear-gradient(160deg,#2f3a2c,#8a8d88 55%,#b5672d)"></div>
<div class="g" role="img" aria-label="Bright lounge with white floor and blue throw" style="left:243px;top:2900px;background:linear-gradient(170deg,#e6e3df,#b8aea3 55%,#eeeeee)"></div>
<div class="g" role="img" aria-label="Long corridor with polished beige floor" style="left:487px;top:2900px;background:linear-gradient(180deg,#d9cbb5,#a88d6e 50%,#e7dccb)"></div>
<div class="g" role="img" aria-label="Lobby with glossy white floor and pendant lights" style="left:728px;top:2900px;background:linear-gradient(180deg,#6b5a44,#d8d4ce 50%,#f0efed)"></div>
<div class="g" role="img" aria-label="Open living area with dark sofa and light floor" style="left:971px;top:2900px;background:linear-gradient(180deg,#ececea,#c7bfb4 55%,#5c5550)"></div>
<div class="g" role="img" aria-label="Marble-look white floor with decorative vase" style="left:0;top:3143px;background:linear-gradient(160deg,#efefef,#cfcac3 60%,#8d857c)"></div>
<div class="g" role="img" aria-label="Black framed glass door beside white wall" style="left:243px;top:3143px;background:linear-gradient(90deg,#1e1e1e 25%,#e7e7e7 45%,#f4f4f4)"></div>
<div class="g" role="img" aria-label="White bathroom vanity with timber shelving" style="left:487px;top:3143px;background:linear-gradient(180deg,#f2f0ec,#d6c2a5 50%,#ebe7e1)"></div>
<div class="g" role="img" aria-label="Grand hall with reflective grey floor and artwork" style="left:728px;top:3143px;background:linear-gradient(180deg,#4b4b4b,#9b9b9b 55%,#dcdcdc)"></div>
<div class="g" role="img" aria-label="Timber staircase with glass rail over white floor" style="left:971px;top:3143px;background:linear-gradient(180deg,#f1efeb,#b97d57 60%,#eae6e0)"></div>
<div class="btn" style="left:521px;top:3422px;width:158px;height:41px">View All Gallery</div>

<!-- Contact -->
<div class="contact-bg"></div>
<svg class="abs" style="left:142px;top:3551px" width="916" height="389" viewBox="0 0 916 389"><path d="M0 389 V120 Q0 80 40 64 L330 6 Q458 -12 586 6 L876 64 Q916 80 916 120 V389 Z" fill="#ec1c24"/></svg>
<section class="contact">
  <h2>Contact Us</h2>
  <div class="field" style="left:354px;top:3697px;width:240px">Your Name*</div>
  <div class="field" style="left:606px;top:3697px;width:240px">Email*</div>
  <div class="field" style="left:354px;top:3744px;width:240px">Phone*</div>
  <div class="field" style="left:606px;top:3744px;width:240px">Inquiry For*</div>
  <div class="field" style="left:354px;top:3792px;width:492px;height:56px">How can we help you?</div>
  <div class="btn" style="left:553px;top:3870px;width:94px;height:33px;background:var(--black);font-weight:600">Submit</div>
</section>

<!-- Footer -->
<nav class="fnav">
  <a class="active" style="left:434px">Home</a>
  <a style="left:513px">Services</a>
  <a style="left:607px">Gallery</a>
  <a style="left:694px">Contact Us</a>
</nav>
<div class="abs" style="left:142px;top:4004px;width:916px;height:1px;background:#555"></div>
<div class="abs" style="left:155px;top:4050px;font-size:30px;font-weight:700;color:var(--white);line-height:1">VENBROOK</div>
<div class="abs" style="left:155px;top:4086px;width:188px;text-align:center;font-size:14px;letter-spacing:2px;color:var(--white)">FINISHES</div>
<div class="fdiv" style="left:387px"></div>
<div class="fdiv" style="left:811px"></div>
<svg class="abs" style="left:420px;top:4052px" width="14" height="18" viewBox="0 0 14 18" fill="none" stroke="#fff" stroke-width="1.5"><path d="M7 17 Q1 10 1 6.5 A6 6 0 0 1 13 6.5 Q13 10 7 17 Z"/><circle cx="7" cy="6.5" r="2"/></svg>
<div class="finfo" style="left:444px;top:4050px">123 Lorem ipsume Dilor<br>Site 32311 Lorem ipsume</div>
<svg class="abs" style="left:664px;top:4054px" width="16" height="16" viewBox="0 0 16 16" fill="none" stroke="#fff" stroke-width="1.5"><path d="M2 2 H5 L6.5 5.5 L4.5 7 Q6 10 9 11.5 L10.5 9.5 L14 11 V14 Q8 15 4.5 11.5 Q1 8 2 2 Z"/></svg>
<div class="finfo" style="left:696px;top:4052px">Call :<br>123 456 7890</div>
<svg class="abs" style="left:844px;top:4054px" width="18" height="14" viewBox="0 0 18 14" fill="none" stroke="#fff" stroke-width="1.5"><rect x="1" y="1" width="16" height="12" rx="1"/><path d="M1 2 L9 8 L17 2"/></svg>
<div class="finfo" style="left:878px;top:4050px">Email :<br>hello@venbrookfinishes.com</div>
<div class="abs" style="left:0;top:4150px;width:1200px;height:1px;background:#333"></div>
<div class="abs" style="left:142px;top:4163px;font-size:12px;color:var(--white)">© 2024 Venbrook Finishes Flooring Home Improvement. All Rights Reserved.</div>
<div class="social" style="left:975px"></div>
<div class="social" style="left:1005px"></div>
<div class="social" style="left:1035px"></div>

</body>
</html>
```